Empower our Electric Journey on the Web

We need a new website that can promote our services. Our three services that we offer are:
- Management of e-mobility charging stations
- Management of energy purchases
- Leasing of E-Mobility charging stations
- Energy billing of private electricity meters
The website should work responsively on PC, tablet and smartphone. In general, a simple navigation and an appealing design should be in the foreground. The website should give the customer the possibility to request , based pm a preset chexkbox chart and to get in contact with us.
Our logo works on black and white background.
Our slogan is:
Empower Your Electric Journey with Velmor Mobility
The 4 Pages should be the following:
Main Page, with info about us, why choose us,
2nd; services; what we sell and what are our services
3rd; Contact us, request an offer
4th, References about costumers and Work we already did, in the future we would like to integrate a Blog Post in this section in stead of references.

Target Market(s)

Landlords, Homeowners, Homeowner Associations

Industry/Entity Type

EV Chargers / E-Mobility

Coding

Coded - Design and coding required

Number of Pages Required

4 page

Requirements
Nice to have
• Pop up to our mailchimp newsletter subscription

```html
<!DOCTYPE html>
<html lang="en">
<head>
<meta charset="utf-8">
<title>Velmor Mobility</title>
<link rel="stylesheet" href="https://fonts.googleapis.com/css2?family=Poppins:wght@400;500;600;700&display=swap">
<style>
:root{
  --green:#3fbf3a;
  --green-dark:#2fa52b;
  --mint:#dcf8d8;
  --ink:#111;
  --text:#555;
  --muted:#f4f4f4;
  --dark:#0b0b0b;
  --white:#fff;
}
*{box-sizing:border-box;margin:0;padding:0}
html,body{width:1200px;height:4823px;overflow:hidden}
body{font-family:'Poppins',sans-serif;color:var(--ink);background:var(--white);position:relative}
a{color:inherit;text-decoration:none}

/* header */
.site-header{position:absolute;top:0;left:0;width:1200px;height:140px;background:var(--white)}
.brand{position:absolute;left:85px;top:50px;display:flex;align-items:center;gap:12px;font-weight:700;font-size:30px;color:var(--green);text-transform:uppercase;letter-spacing:1px;white-space:nowrap}
.brand-mark{width:22px;height:22px;background:var(--green)}
.main-nav{position:absolute;top:66px;left:511px;display:flex;font-size:15px;color:#333;white-space:nowrap}
.main-nav a{position:relative;margin-right:36px}
.main-nav a.active{color:var(--green)}
.main-nav a.active::after{content:"";position:absolute;left:-5px;right:-5px;top:38px;height:3px;background:var(--green)}
.caret{font-size:10px}

/* hero */
.hero{position:absolute;top:140px;left:0;width:1200px;height:669px;background:linear-gradient(120deg,#6c6c6c 0%,#4a4a4a 45%,#3a3a3a 70%,#565656 100%)}
.hero h1{position:absolute;top:255px;width:100%;text-align:center;color:var(--white);font-size:40px;font-weight:600;line-height:50px;text-transform:uppercase}
.btn{display:inline-flex;align-items:center;justify-content:center;background:var(--green);color:var(--white);font-weight:500;border-radius:10px;white-space:nowrap}
.hero .btn{position:absolute;left:492px;top:395px;width:215px;height:73px;font-size:20px}
.slide-arrow{position:absolute;width:50px;height:64px;border:2px solid var(--white);border-radius:4px;display:flex;align-items:center;justify-content:center}
.hero .prev{left:34px;top:316px}
.hero .next{left:1113px;top:316px;border-color:var(--green)}

/* section titles */
.section-title{position:absolute;width:100%;text-align:center;font-size:46px;font-weight:700;text-transform:uppercase;letter-spacing:-1px}
.section-title span{color:var(--green)}

/* services */
.service{position:absolute;width:480px;height:150px}
.service-icon{position:absolute;left:0;top:0;width:142px;height:142px;border-radius:50%;border:9px solid #e8f7e6;background:var(--white);display:flex;align-items:center;justify-content:center}
.service-icon.grey{border-color:#e9e9e9}
.service h3{position:absolute;left:165px;top:0;font-size:19px;font-weight:500;line-height:25px;width:300px}
.service p{position:absolute;left:165px;top:64px;width:320px;font-size:14.5px;line-height:23px;color:var(--text);text-align:justify}

/* about */
.about-band{position:absolute;top:1520px;left:0;width:1200px;height:554px;background:linear-gradient(180deg,#aed6a8 0%,#c8e6c2 60%,#d4ecd0 100%)}
.lower-bg{position:absolute;top:2074px;left:0;width:1200px;height:777px;background:var(--muted)}
.about-card{position:absolute;top:1681px;left:103px;width:992px;height:513px;background:var(--white)}
.about-photo{position:absolute;left:13px;top:11px;width:440px;height:488px;background:linear-gradient(160deg,#6f7d66 0%,#d7dde0 45%,#c96b2c 70%,#8b8f86 100%)}
.about-card h2{position:absolute;left:508px;top:90px;font-size:38px;font-weight:700;text-transform:uppercase}
.about-card h2 span{color:var(--green)}
.about-card p{position:absolute;left:508px;top:153px;width:400px;font-size:14.5px;line-height:31px;color:var(--text);text-align:justify}
.about-card .btn{position:absolute;left:509px;top:390px;width:151px;height:57px;font-size:14px}

/* why */
.why-box{position:absolute;top:2493px;width:320px;height:240px;border:1.5px dashed #555;background:var(--muted)}
.why-icon{position:absolute;left:34px;top:-40px;width:90px;height:90px;border-radius:50%;border:2px solid #222;background:var(--white);display:flex;align-items:center;justify-content:center}
.why-box h3{position:absolute;left:33px;top:82px;font-size:23px;font-weight:500;white-space:nowrap}
.why-box p{position:absolute;left:33px;top:126px;width:258px;font-size:14.5px;line-height:25px;color:var(--text);text-align:justify}

/* request */
.request{position:absolute;top:2851px;left:0;width:1200px;height:552px;background:linear-gradient(180deg,#151515,#222 60%,#1a1a1a);color:var(--white)}
.request .section-title{top:112px}
.request p{position:absolute;top:242px;width:100%;text-align:center;font-size:15px;line-height:31px}
.request .check{position:absolute;left:438px;top:380px}
.request .btn{position:absolute;left:509px;top:376px;width:251px;height:63px;font-size:20px}

/* blog */
.blog-card{position:absolute;top:3637px;width:318px}
.blog-photo{width:318px;height:201px;position:relative}
.date{position:absolute;left:0;top:0;background:var(--white);color:var(--green);font-size:10px;font-weight:600;padding:6px 14px;border-radius:0 0 12px 0}
.blog-card h3{margin-top:34px;font-size:16px;font-weight:500;color:var(--green);text-transform:uppercase}
.blog-card p{margin-top:6px;font-size:15px;line-height:21px;color:#333}
.blog-card .more{display:inline-block;margin:10px 0 0 4px;font-size:12.5px;color:var(--green);text-decoration:underline}
.blog-arrow{position:absolute;top:3745px;width:48px;height:58px;border:1px solid #333;background:#000;display:flex;align-items:center;justify-content:center;border-radius:3px}

/* newsletter + footer */
.footer{position:absolute;top:4208px;left:0;width:1200px;height:538px;background:#000;color:var(--white)}
.newsletter{position:absolute;top:4081px;left:180px;width:840px;height:343px;background:var(--mint);border-radius:6px;text-align:center}
.newsletter h2{margin-top:78px;font-size:39px;font-weight:500}
.newsletter p{margin-top:8px;font-size:14px}
.subscribe{position:absolute;left:95px;top:207px;width:647px;height:69px;background:var(--white);border:1px solid #ddd;border-radius:35px}
.subscribe span{position:absolute;left:40px;top:24px;font-size:14px;color:#777}
.subscribe .signup{position:absolute;right:-1px;top:-1px;width:196px;height:69px;background:#000;color:var(--white);border-radius:35px;font-size:22px;font-weight:500;display:flex;align-items:center;justify-content:center}
.footer .brand{left:92px;top:346px;color:var(--green)}
.footer-col{position:absolute;top:282px}
.footer-col h4{font-size:20px;font-weight:500;color:var(--green)}
.footer-col h4::after{content:"";display:block;width:40px;height:2px;margin-top:6px;background:var(--green)}
.links li{list-style:none;font-size:14px;margin-top:14px;padding-left:22px;position:relative}
.links li::before{content:"›";position:absolute;left:2px;top:-2px}
.contact-item,.social-item{display:flex;align-items:center;gap:18px;margin-top:20px;font-size:14px;line-height:17px;white-space:nowrap}
.ic{width:34px;height:34px;border:1.5px solid #444;border-radius:4px;display:flex;align-items:center;justify-content:center;flex:none}
.sq{width:12px;height:12px;background:var(--green)}
.copyright{position:absolute;top:4746px;left:0;width:1200px;height:77px;background:var(--green);color:var(--white);font-size:13px;text-align:center;line-height:77px}
</style>
</head>
<body>

<header class="site-header">
  <div class="brand"><span class="brand-mark"></span>Velmor Mobility</div>
  <nav class="main-nav">
    <a class="active">Home</a><a>About Us</a><a>Services <span class="caret">▼</span></a><a>Why Choose Us</a><a>Contact Us</a><a>Blog</a>
  </nav>
</header>

<section class="hero" role="img" aria-label="Electric car charging at a public charging station">
  <h1>Empower Your Electric<br>Journey with Velmor Mobility</h1>
  <a class="btn">KNOW MORE</a>
  <span class="slide-arrow prev"><svg width="14" height="14" viewBox="0 0 14 14"><path d="M9 2 4 7l5 5" fill="none" stroke="#fff" stroke-width="2"/></svg></span>
  <span class="slide-arrow next"><svg width="14" height="14" viewBox="0 0 14 14"><path d="M5 2l5 5-5 5" fill="none" stroke="#3fbf3a" stroke-width="2"/></svg></span>
</section>

<h2 class="section-title" style="top:932px"><span>Our</span> Services</h2>

<div class="service" style="left:95px;top:1076px">
  <div class="service-icon"><svg width="56" height="56" viewBox="0 0 56 56" fill="none" stroke="#3fbf3a" stroke-width="2.5"><rect x="12" y="8" width="22" height="36" rx="2"/><rect x="17" y="14" width="12" height="12"/><path d="M8 48h30M34 18h6v18a4 4 0 0 0 8 0V14"/></svg></div>
  <h3>Management of e-mobility charging stations</h3>
  <p>Lorem ipsum dolor sit amet, consectetur adipiscing elit. Quisque eget sollicitudin sem. Ut dictum ipsum a bus.</p>
</div>
<div class="service" style="left:630px;top:1076px">
  <div class="service-icon grey"><svg width="56" height="56" viewBox="0 0 56 56" fill="none" stroke="#111" stroke-width="3"><path d="M44 20a18 18 0 1 0 2 14"/><path d="M30 14 22 30h10l-6 14"/></svg></div>
  <h3>Management of energy purchases</h3>
  <p>Lorem ipsum dolor sit amet, consectetur adipiscing elit. Quisque eget sollicitudin sem. Ut dictum ipsum a bus.</p>
</div>
<div class="service" style="left:95px;top:1268px">
  <div class="service-icon grey"><svg width="56" height="56" viewBox="0 0 56 56" fill="none" stroke="#111" stroke-width="3"><rect x="12" y="10" width="24" height="30" rx="2"/><path d="M8 46h32M36 20h8v14"/><circle cx="44" cy="10" r="4" fill="#111"/></svg></div>
  <h3>Leasing of E-Mobility charging stations</h3>
  <p>Lorem ipsum dolor sit amet, consectetur adipiscing elit. Quisque eget sollicitudin sem. Ut dictum ipsum a bus.</p>
</div>
<div class="service" style="left:630px;top:1268px">
  <div class="service-icon"><svg width="56" height="56" viewBox="0 0 56 56" fill="none" stroke="#3fbf3a" stroke-width="2.5"><circle cx="20" cy="34" r="12"/><rect x="24" y="12" width="24" height="12" rx="6"/><path d="M20 28v12M40 6l-4 6h6l-4 6"/></svg></div>
  <h3>Energy billing of private electricity meters</h3>
  <p>Lorem ipsum dolor sit amet, consectetur adipiscing elit. Quisque eget sollicitudin sem. Ut dictum ipsum a bus.</p>
</div>

<div class="about-band" role="img" aria-label="Parking lot with electric cars, tinted green"></div>
<div class="lower-bg"></div>
<section class="about-card">
  <div class="about-photo" role="img" aria-label="Orange and white charging station with cable"></div>
  <h2><span>About</span> Us</h2>
  <p>Lorem ipsum dolor sit amet, consectetur adipiscing elit, sed do eiusmod tempor incididunt ut labore et dolore magna aliqua. Ut enim ad minim veniam, quis nostrud exercitation ullamco laboris nisi ut aliquip ex ea commodo consequat. Duis aute irure dolor in reprehenderit in voluptate velit esse cillum dolore eu fugiat nulla pariatur.</p>
  <a class="btn">READ MORE</a>
</section>

<h2 class="section-title" style="top:2316px"><span>Why</span> Choose Us?</h2>
<div class="why-box" style="left:95px">
  <span class="why-icon"><svg width="40" height="40" viewBox="0 0 40 40"><circle cx="20" cy="15" r="8" fill="#3fbf3a"/><path d="M6 38a14 12 0 0 1 28 0z" fill="#111"/><path d="M10 16a10 10 0 0 1 20 0" fill="none" stroke="#111" stroke-width="2.5"/></svg></span>
  <h3>24/7 Customer Service</h3>
  <p>Lorem ipsum dolor sit amet, con sectetur adipiscing elit. Quisque eget sollicitudin sem.</p>
</div>
<div class="why-box" style="left:440px">
  <span class="why-icon"><svg width="40" height="40" viewBox="0 0 40 40"><path d="M20 3 5 9v10c0 9 7 15 15 18 8-3 15-9 15-18V9z" fill="#3fbf3a"/><path d="m13 20 5 5 9-10" fill="none" stroke="#fff" stroke-width="3"/></svg></span>
  <h3>Premium Protection</h3>
  <p>Lorem ipsum dolor sit amet, con sectetur adipiscing elit. Quisque eget sollicitudin sem.</p>
</div>
<div class="why-box" style="left:784px">
  <span class="why-icon"><svg width="40" height="40" viewBox="0 0 40 40"><circle cx="20" cy="15" r="11" fill="#3fbf3a"/><path d="M13 24 9 37l6-3 3 5 2-12M27 24l4 13-6-3-3 5-2-12" fill="#111"/></svg></span>
  <h3>Quality Assured</h3>
  <p>Lorem ipsum dolor sit amet, con sectetur adipiscing elit. Quisque eget sollicitudin sem.</p>
</div>

<section class="request" role="img" aria-label="Dark background with charging stations">
  <h2 class="section-title"><span>Request</span> an Offer</h2>
  <p>Lorem ipsum dolor sit amet, consectetur adipiscing elit. Quisque eget sollicitudin sem.<br>Ut dictum ipsum a elementum finibus. Nam tristique magna porttitor porta finibus.<br>Cras at varius ante, id finibus massa.</p>
  <svg class="check" width="46" height="46" viewBox="0 0 46 46" fill="none" stroke="#fff" stroke-width="4"><path d="M34 24v16H6V12h22"/><path d="m12 22 9 9 20-24"/></svg>
  <a class="btn">REQUEST A SERVICE</a>
</section>

<h2 class="section-title" style="top:3514px"><span>Our</span> Blog</h2>
<span class="blog-arrow" style="left:25px"><svg width="12" height="14"><path d="M9 2 4 7l5 5" fill="none" stroke="#3fbf3a" stroke-width="2"/></svg></span>
<span class="blog-arrow" style="left:1124px"><svg width="12" height="14"><path d="M3 2l5 5-5 5" fill="none" stroke="#3fbf3a" stroke-width="2"/></svg></span>
<article class="blog-card" style="left:103px">
  <div class="blog-photo" role="img" aria-label="Electric car front in a dark garage" style="background:linear-gradient(135deg,#3a3a3a,#111 60%,#555)"><span class="date">▣ Feb 20, 2023</span></div>
  <h3>Lorem ipsum dolor sit amet</h3>
  <p>Lorem ipsum dolor sit amet, consecte tur adipiscing elit. Quisque eget sollic itudin sem.</p>
  <a class="more">READ MORE</a>
</article>
<article class="blog-card" style="left:443px">
  <div class="blog-photo" role="img" aria-label="Woman plugging a charger into a car" style="background:linear-gradient(135deg,#5b6f86,#c9b8a0 55%,#2f3e52)"><span class="date">▣ Feb 20, 2023</span></div>
  <h3>Lorem ipsum dolor sit amet</h3>
  <p>Lorem ipsum dolor sit amet, consecte tur adipiscing elit. Quisque eget sollic itudin sem.</p>
  <a class="more">READ MORE</a>
</article>
<article class="blog-card" style="left:784px">
  <div class="blog-photo" role="img" aria-label="White SUV parked at a wall charger" style="background:linear-gradient(135deg,#a09a90,#e0e0e0 55%,#6e7d5c)"><span class="date">▣ Feb 20, 2023</span></div>
  <h3>Lorem ipsum dolor sit amet</h3>
  <p>Lorem ipsum dolor sit amet, consecte tur adipiscing elit. Quisque eget sollic itudin sem.</p>
  <a class="more">READ MORE</a>
</article>

<footer class="footer">
  <div class="brand"><span class="brand-mark"></span>Velmor Mobility</div>
  <div class="footer-col" style="left:476px">
    <h4>Quick Links</h4>
    <ul class="links"><li>Home</li><li>About Us</li><li>Services</li><li>Contact Us</li></ul>
  </div>
  <div class="footer-col" style="left:674px">
    <h4>Contact Us</h4>
    <div class="contact-item"><span class="ic"><svg width="14" height="14" viewBox="0 0 14 14"><path d="M3 1l2 3-1 2a7 7 0 0 0 4 4l2-1 3 2-1 2C6 13 1 8 1 2z" fill="#3fbf3a"/></svg></span><span>CALL US<br>8012 555 0190</span></div>
    <div class="contact-item"><span class="ic"><svg width="14" height="12"><rect x="1" y="1" width="12" height="10" fill="none" stroke="#3fbf3a" stroke-width="1.5"/><path d="m1 1 6 5 6-5" fill="none" stroke="#3fbf3a" stroke-width="1.5"/></svg></span><span>EMAIL US<br>info@velmormobility.com</span></div>
    <div class="contact-item"><span class="ic"><svg width="12" height="16"><path d="M6 15s5-6 5-9a5 5 0 0 0-10 0c0 3 5 9 5 9z" fill="#3fbf3a"/><circle cx="6" cy="6" r="2" fill="#000"/></svg></span><span>Address line Dummy Here<br>Address line Here</span></div>
  </div>
  <div class="footer-col" style="left:970px">
    <h4>Follow Us</h4>
    <div class="social-item"><span class="ic"><span class="sq"></span></span>LINKWAVE</div>
    <div class="social-item"><span class="ic"><span class="sq"></span></span>CHATTERLY</div>
    <div class="social-item"><span class="ic"><span class="sq"></span></span>PHOTOVERSE</div>
  </div>
</footer>

<section class="newsletter">
  <h2>Our Newsletter Sign Up</h2>
  <p>Subscribe our newsletter to get the latest news and updates</p>
  <div class="subscribe"><span>Enter Email Address</span><a class="signup">SIGNUP</a></div>
</section>

<div class="copyright">Copyright © 2023 All Rights Reserved By Velmor Mobility</div>

</body>
</html>
```